Poster design for - Glowing Meadow Festival

To design a dynamic illustrated Glowing Meadow Festival poster.
The dates are: 3-5 July 2020
Location: Tarlow Campsite, Fennick, Wendshire
www.glowingmeadow.co.uk

Here is some text about the event to give you an idea. You can take elements from it if you like:

A Gathering of Female Energy to Ignite and Embrace the Power of Woman with Mother Earth.

Target Market(s)

Women festival goers.

Industry/Entity Type

Festival

Colors

Designer to choose colors to be used in the design.

Requirements
Must have
• Glowing Meadow Logo - but this can be altered to look washed out.
• Date, location, website url.
Nice to have
• Earthy, hippy, festival look.

```html
<!DOCTYPE html>
<html lang="en">
<head>
<meta charset="utf-8">
<title>Glowing Meadow Festival 2020 Poster</title>
<link rel="stylesheet" href="https://fonts.googleapis.com/css2?family=Exo+2:wght@700&family=Saira+Condensed:wght@600;700&family=Roboto:wght@300;400&display=swap">
<style>
  :root {
    --page: #d9d8d4;
    --edge: #050303;
    --ink: #0a0504;
    --ember-deep: #3a0f04;
    --ember: #b9440d;
    --flame: #f04e23;
    --amber: #e07a0c;
    --gold: #f3a21c;
    --white: #ffffff;
    --muted: #e9d7c9;
  }
  * { box-sizing: border-box; margin: 0; padding: 0; }
  html, body { width: 1200px; height: 1148px; overflow: hidden; background: var(--page); }
  .poster {
    position: absolute; left: 210px; top: 24px; width: 780px; height: 1100px;
    background: var(--edge); padding: 12px;
  }
  .poster-inner {
    position: relative; width: 100%; height: 100%; overflow: hidden;
    background:
      radial-gradient(ellipse 80% 45% at 50% 100%, var(--ember) 0%, var(--ember-deep) 45%, transparent 80%),
      linear-gradient(180deg, #130806 0%, var(--ink) 45%, #1c0904 100%);
  }
  .hex-backdrop {
    position: absolute; left: 90px; top: 40px; width: 576px; height: 300px;
    background: radial-gradient(ellipse at 50% 50%, rgba(150,20,10,0.35) 0%, rgba(80,10,5,0.15) 55%, transparent 75%);
  }
  .embers {
    position: absolute; left: 0; right: 0; top: 640px; bottom: 0;
    background: radial-gradient(ellipse 70% 60% at 50% 80%, rgba(240,120,30,0.18), transparent 70%);
  }
  .brand {
    position: absolute; left: 0; right: 0; top: 118px; text-align: center;
  }
  .brand-mark {
    display: block; width: 110px; height: 110px; margin: 0 auto 44px;
    border-radius: 50%; background: var(--flame);
  }
  .brand-name {
    font-family: "Roboto", sans-serif; font-weight: 300; color: var(--white);
    text-transform: uppercase; line-height: 1;
  }
  .brand-name-main {
    display: block; font-size: 56px; letter-spacing: 7px; margin-left: 7px;
  }
  .brand-name-sub {
    display: block; margin-top: 48px; font-size: 44px; letter-spacing: 36px; margin-left: 36px;
  }
  .year {
    position: absolute; left: 0; right: 0; top: 548px; text-align: center;
    font-family: "Exo 2", sans-serif; font-weight: 700; font-size: 150px; line-height: 1;
    letter-spacing: 6px;
    background: linear-gradient(180deg, #8a4a14 0%, var(--amber) 55%, var(--gold) 100%);
    -webkit-background-clip: text; background-clip: text; color: transparent;
  }
  .dates {
    position: absolute; left: 240px; top: 706px; width: 290px; height: 118px;
    background: var(--amber); display: flex; align-items: center; padding: 8px;
    box-shadow: 0 6px 14px rgba(0,0,0,0.5);
  }
  .dates-days {
    background: var(--edge); color: var(--white); height: 100%; width: 84px;
    font-family: "Saira Condensed", sans-serif; font-weight: 600; font-size: 42px;
    line-height: 48px; display: flex; flex-direction: column; justify-content: center; align-items: center;
  }
  .dates-month {
    flex: 1; text-align: center; color: var(--white);
    font-family: "Saira Condensed", sans-serif; font-weight: 700; font-size: 104px; line-height: 1;
  }
  .location {
    position: absolute; left: 0; right: 0; top: 880px; text-align: center;
  }
  .location-label {
    display: inline-block; padding: 5px 4px;
    border-top: 1px solid var(--amber); border-bottom: 1px solid var(--amber);
    font-family: "Roboto", sans-serif; font-weight: 300; font-size: 17px; letter-spacing: 3px;
    color: var(--muted); text-transform: uppercase;
  }
  .location-address {
    margin-top: 22px; font-family: "Roboto", sans-serif; font-weight: 400;
    font-size: 24px; color: var(--white);
  }
  .web-bar {
    position: absolute; left: 0; right: 0; top: 1004px; height: 56px;
    background: rgba(10,5,4,0.82); display: flex; align-items: center; justify-content: center;
    font-family: "Roboto", sans-serif; font-weight: 400; font-size: 19px; letter-spacing: 3.5px;
    color: var(--white);
  }
</style>
</head>
<body>
  <div class="poster">
    <div class="poster-inner">
      <div class="hex-backdrop" role="img" aria-label="Dark red honeycomb pattern glowing behind the festival name"></div>
      <div class="embers" role="img" aria-label="Rising fire sparks and glowing embers"></div>

      <div class="brand">
        <span class="brand-mark"></span>
        <h1 class="brand-name">
          <span class="brand-name-main">Glowing Meadow</span>
          <span class="brand-name-sub">Festival</span>
        </h1>
      </div>

      <div class="year">2020</div>

      <div class="dates">
        <div class="dates-days"><span>3RD</span><span>5TH</span></div>
        <div class="dates-month">JULY</div>
      </div>

      <div class="location">
        <span class="location-label">Festival Location</span>
        <p class="location-address">Tarlow Campsite, Fennick, Wendshire</p>
      </div>

      <div class="web-bar">www.glowingmeadow.co.uk</div>
    </div>
  </div>
</body>
</html>
```